Awesome new dental practice requires a New Letterhead design

We would like a new letterhead design to align with our new business branding & business cards. I have uploaded all the logos & current business card details that can be used. The new website can be viewed here https://kelvora.com.au

Other useful details: Font Poppins
Colour Palettes:
Dark Pink #c45389
Light Pink: #e83e8c
Black

Please let me know if you have any questions or require anything else.

Dental

• Poppins

```html
<!DOCTYPE html>
<html lang="en">
<head>
<meta charset="utf-8">
<title>Kelvora Letterhead</title>
<link href="https://fonts.googleapis.com/css2?family=Mulish:wght@400;500&family=Poppins:wght@400;500;600;700&display=swap" rel="stylesheet">
<style>
  :root {
    --bg: #e6e6e6;
    --paper: #f4f4f4;
    --ink: #222222;
    --body: #4a4a4a;
    --pink: #e83e8c;
    --pink-dark: #c45389;
    --seal: #7c97d8;
    --seal-fill: #eef1f9;
  }
  * { margin: 0; padding: 0; box-sizing: border-box; }
  html, body {
    width: 1200px; height: 794px; overflow: hidden;
    background: var(--bg);
    font-family: "Poppins", sans-serif;
  }
  .letterhead {
    position: absolute; left: 337px; top: 27px;
    width: 526px; height: 740px;
    background: var(--paper);
    box-shadow: 0 2px 8px rgba(0,0,0,0.12);
  }
  .brand { position: absolute; left: 49px; top: 38px; }
  .brand-name {
    font-size: 22px; font-weight: 600; color: var(--ink);
    letter-spacing: -0.5px; line-height: 1;
  }
  .brand-descriptor {
    margin-top: 6px; font-size: 6.5px; font-weight: 600;
    letter-spacing: 1.3px; color: var(--ink);
  }
  .letter-body {
    position: absolute; left: 47px; top: 205px; width: 438px;
    font-family: "Mulish", sans-serif;
    font-size: 9.8px; line-height: 15.2px; color: var(--body);
  }
  .letter-body p + p { margin-top: 15px; }
  .sign-off {
    position: absolute; left: 413px; top: 492px;
    font-family: "Mulish", sans-serif;
    font-size: 9.8px; color: var(--body);
  }
  .seal { position: absolute; left: 381px; top: 516px; }
  .contact { position: absolute; left: 50px; top: 620px; }
  .contact-rule { width: 18px; height: 2px; background: var(--pink); }
  .contact-title {
    margin-top: 8px; font-size: 11px; font-weight: 700;
    letter-spacing: 1px; color: var(--ink);
  }
  .contact-list { list-style: none; margin-top: 4px; }
  .contact-list li {
    display: flex; align-items: flex-start; gap: 6px;
    font-size: 8px; line-height: 14px; font-weight: 500; color: var(--ink);
  }
  .contact-list svg { flex: none; margin-top: 3px; }
  .tagline {
    position: absolute; right: 36px; top: 677px; text-align: right;
    font-size: 12.5px; font-weight: 600; letter-spacing: 1.1px;
    line-height: 21px; color: var(--ink);
  }
  .tagline .accent { color: var(--pink); }
</style>
</head>
<body>
  <main class="letterhead">
    <header class="brand">
      <div class="brand-name">Kelvora</div>
      <div class="brand-descriptor">DENTISTRY &amp; ORTHODONTICS</div>
    </header>

    <section class="letter-body">
      <p>Lorem ipsum dolor sit amet, consectetur adipiscing elit. Donec orci purus, luctus vitae dignissim eu, iaculis sed purus. Vivamus faucibus, ipsum nec aliquet viverra, leo mauris condimentum ligula, sit amet sagittis enim ligula quis arcu. Nam egestas tortor id nisi porttitor mattis. In tortor ante, ultricies in suscipit a, tempus non massa. Vivamus et auctor mi. Fusce vel massa nulla. Phasellus nec eros mauris, et scelerisque orci.</p>
      <p>Donec malesuada orci vitae nulla accumsan porta a id massa. Quisque accumsan iaculis magna sit amet fringilla. Maecenas consequat, magna eget tincidunt semper, odio nibh rutrum mi, id feugiat ante nisi eu risus. Vestibulum nunc orci, rhoncus a placerat in, ultricies in mi. Cras mattis varius eros, vel fringilla nisi suscipit eget. Quisque scelerisque sagittis nulla at porttitor.</p>
      <p>Sed id augue vitae urna euismod commodo aliquet a quam. Pellentesque arcu velit, cursus et malesuada ut, consequat et diam. Nullam erat sem, rhoncus id ullamcorper vitae, rhoncus et arcu. In ultricies ultricies nulla, ut rutrum nisi iaculis at. Donec eu magna a metus ornare faucibus. Fusce aliquet faucibus ultricies. Morbi semper, est id tincidunt gravida, sem arcu adipiscing lacus, ac bibendum nulla leo eu purus. Quisque nec diam sed risus consectetur a ccumsan quis quis nibh. Vestibulum id purus lorem.</p>
    </section>

    <div class="sign-off">Sincerily,</div>
    <svg class="seal" width="78" height="78" viewBox="0 0 78 78" role="img" aria-label="Notary seal with the dentist's handwritten signature">
      <circle cx="39" cy="39" r="37" fill="var(--seal-fill)" stroke="var(--seal)" stroke-width="1.6"/>
    </svg>

    <footer class="contact">
      <div class="contact-rule"></div>
      <h2 class="contact-title">CONTACT US</h2>
      <ul class="contact-list">
        <li>
          <svg width="8" height="8" viewBox="0 0 24 24"><path fill="var(--ink)" d="M6.6 10.8a15 15 0 0 0 6.6 6.6l2.2-2.2a1 1 0 0 1 1-.25 11.4 11.4 0 0 0 3.6.57 1 1 0 0 1 1 1V20a1 1 0 0 1-1 1A17 17 0 0 1 3 4a1 1 0 0 1 1-1h3.5a1 1 0 0 1 1 1c0 1.25.2 2.45.57 3.57a1 1 0 0 1-.25 1z"/></svg>
          <span>(08) 9000 4812</span>
        </li>
        <li>
          <svg width="8" height="8" viewBox="0 0 24 24"><path fill="var(--ink)" d="M2 5h20v14H2zm2 2v.5l8 5 8-5V7l-8 5z"/></svg>
          <span>hello@kelvora.com.au</span>
        </li>
        <li>
          <svg width="8" height="8" viewBox="0 0 24 24"><path fill="var(--ink)" d="M12 2a7 7 0 0 0-7 7c0 5 7 13 7 13s7-8 7-13a7 7 0 0 0-7-7zm0 9.5A2.5 2.5 0 1 1 12 6.5a2.5 2.5 0 0 1 0 5z"/></svg>
          <span>Shop 7, 22 Marlin Street<br>Karratha WA</span>
        </li>
        <li>
          <svg width="8" height="8" viewBox="0 0 24 24"><circle cx="12" cy="12" r="9" fill="none" stroke="var(--ink)" stroke-width="2.5"/><path d="M3 12h18M12 3c3 3 3 15 0 18M12 3c-3 3-3 15 0 18" fill="none" stroke="var(--ink)" stroke-width="2"/></svg>
          <span>kelvora.com.au</span>
        </li>
      </ul>
    </footer>

    <div class="tagline">
      <div>Life is short.</div>
      <div><span class="accent">Smile</span> while you still have teeth.</div>
    </div>
  </main>
</body>
</html>
```